Business Card and Simple Logo Desgin

New Zealand based start up company "Brook Advisory LTD" requires business cards and simple logo design.

Card Content.

Brook Advisory LTD

Joanna Pritchard
CA, BMS (Hons)

j.pritchard@brookadvisory.co.nz
PH +64 21 574 160

Target Market(s)

Corporate Business in IT, Finance and accounting.

Industry/Entity Type

Business

```html
<!DOCTYPE html>
<html lang="en">
<head>
<meta charset="utf-8">
<title>Brook Advisory LTD — Business Card</title>
<link rel="stylesheet" href="https://fonts.googleapis.com/css2?family=Montserrat:wght@400;500&display=swap">
<style>
  :root {
    --page-bg: #e9e6e3;
    --card-white: #ffffff;
    --card-navy: #0a1a47;
    --ink-navy: #1c2a6b;
    --ink-soft: #6f7fc4;
    --dot-lilac: #c9cbe6;
    --dot-pale: #e6ecf6;
    --mark-white: #ffffff;
    --shadow: rgba(40, 30, 20, 0.18);
  }

  * { margin: 0; padding: 0; box-sizing: border-box; }

  html, body {
    width: 1200px;
    height: 900px;
    overflow: hidden;
  }

  body {
    background: var(--page-bg);
    font-family: "Montserrat", Arial, sans-serif;
    display: flex;
    flex-direction: column;
    align-items: center;
    justify-content: center;
    gap: 56px;
  }

  .card {
    position: relative;
    width: 580px;
    height: 352px;
    border-radius: 4px;
    box-shadow: 0 10px 28px var(--shadow);
    overflow: hidden;
  }

  /* Front side */
  .card--front { background: var(--card-white); }

  .card__pattern-area {
    position: absolute;
    left: 0;
    top: 0;
    width: 200px;
    height: 100%;
    background: radial-gradient(ellipse at 80% 45%, var(--dot-lilac) 0%, var(--dot-pale) 45%, var(--card-white) 78%);
  }

  .brand {
    position: absolute;
    top: 54px;
    right: 44px;
    display: flex;
    align-items: center;
    gap: 10px;
  }

  .brand__dot {
    width: 22px;
    height: 22px;
    border-radius: 50%;
    background: var(--ink-navy);
  }

  .brand__name {
    font-size: 19px;
    font-weight: 500;
    letter-spacing: 0.02em;
    text-transform: uppercase;
    color: var(--ink-navy);
  }

  .holder {
    position: absolute;
    top: 132px;
    right: 44px;
    text-align: right;
  }

  .holder__name {
    font-size: 20px;
    font-weight: 400;
    letter-spacing: 0.12em;
    text-transform: uppercase;
    color: var(--ink-navy);
  }

  .holder__credentials {
    margin-top: 4px;
    font-size: 12px;
    letter-spacing: 0.12em;
    text-transform: uppercase;
    color: var(--ink-soft);
  }

  .contact {
    position: absolute;
    bottom: 46px;
    right: 44px;
    text-align: right;
    font-size: 13.5px;
    line-height: 1.75;
    color: var(--ink-navy);
    letter-spacing: 0.04em;
  }

  .contact__label { color: var(--ink-navy); }
  .contact__value { color: var(--ink-soft); }

  /* Back side */
  .card--back {
    background: var(--card-navy);
    display: flex;
    flex-direction: column;
    align-items: center;
    justify-content: center;
    gap: 26px;
  }

  .back-mark {
    width: 96px;
    height: 96px;
    border-radius: 50%;
    background: var(--mark-white);
  }

  .back-name {
    font-size: 27px;
    font-weight: 500;
    letter-spacing: 0.02em;
    text-transform: uppercase;
    color: var(--mark-white);
  }
</style>
</head>
<body>

  <section class="card card--front" aria-label="Business card front">
    <div class="card__pattern-area" role="img" aria-label="Decorative arc of soft lilac and pale blue dots"></div>

    <div class="brand">
      <span class="brand__dot"></span>
      <span class="brand__name">Brook Advisory LTD</span>
    </div>

    <div class="holder">
      <p class="holder__name">Joanna Pritchard</p>
      <p class="holder__credentials">CA, BMS (Hons)</p>
    </div>

    <div class="contact">
      <p><span class="contact__label">PH</span> <span class="contact__value">+64 21 574 160</span></p>
      <p class="contact__value">j.pritchard@brookadvisory.co.nz</p>
    </div>
  </section>

  <section class="card card--back" aria-label="Business card back">
    <span class="back-mark"></span>
    <p class="back-name">Brook Advisory LTD</p>
  </section>

</body>
</html>
```